Webdesign for recipe site

Please take a look at www.pfannenwelt.com. PW is a community site with around 60000 user recipes. It is a one-man-project and needs a redesign.
The new design shall meet these facts
high usability
1st focus on content
2nd focus on search and registration-elements
flat menü ? much content above the fold
well contured font type, size and color
coherent button, box and element design
useful design guide for the whole site
flexible font-sizes (changable css)
flexible color set for day and night mode (changable css)
And these facts shall not change
Keeping the „soul“ of pfannenwelt. PW is an independent and free recipe source. No media corporation. Everyone can participate.
This means, that PW is seen as a very personal, even private website and the design shall transport this. The design shall not be cold or heartless. It shall work and leave a cheerful impression as well. The design shall keep the atmosphere of a one-man-project, where everyone is welcomed and the personal touch is warm and heartly.
Since 8 years, the major color is red. The tone must be kept while the intensitity shall be lowered. A decent background and a warm and welltought color set are wanted in a way, that the tone of the website is still seen as red. Probably the links shall remain red, that way the rest can be set less intense.
And these facts are open
The design elements are the cook and the red tomato. While it would be nice to keep the cook (not required at any means), the tomato could be dropped. If they fit into a new design – great, if not, it's ok.
Example Pages
Recipe: http://www.pfannenwelt.com/r/68765-panini-vereinfachte-variation.html
Category: http://www.pfannenwelt.com/kb/0k0/Backrezept/rezepte.html
Homepage: http://www.pfannenwelt.com
Updates
A nice color set: http://www.artfolkhub.com/design/463831
A well structured design: http://www.artfolkhub.com/design/452858
Reason: Just 3 days left and no submission yet.
We will guarantee the project payment (thanks for hinting, Tomas) and extend the deadline by 7 days.
Thank you for your submissions.
The brown/red/beige color-sets are good, they lead the way. The layout though is mostly too playful. It shall be clean and simple and likely to fit for all the content, for the single recipe as well as the recipe lists, the profile page and the homepage.
I got inspired by you color sets and set up a testpage that pretty much goes in to the direction I want. Very flat header, peaceful and warm colors, no distraction, focus on the content. What's still missing is the breadcrumb section and an idea to fill the homepage and the recipe lists. And probably the colors (especially the light background-color, is it beige?) can also be better choosen.
Please see http://www.pfannenwelt.com/test-543677423/r_v01.html
Kind regards, Lukas
Reason: I extend the deadline once more to give Wurl Studio the opportunity to participate. It would be nice to see drafts that go more into the clean and simple direction as I updated in the brief. Here is the current status: http://www.pfannenwelt.com/r/60262-steak-auf-spargel.html (is on test now). Maybe the beige-colors can be choosen more cleaner and suggestions for the homepage and recipe lists and the footer are very welcome also. Looking forward for your designs!
I'll put the Feedback on the latest design of quietmaple in the brief, so you all find it.
http://www.artfolkhub.com/design/587249/web-design-by-quietmaple
-
Dont't know man, this still doesn't look as clean as I need it. There are 100s of recipe sites online and it is urgent to design the page with clear focus on the content. As little distraction as possible, there will be ads for that.
Mainly, you did too much. There are too many design elements and the round bites with the squares. The header shall be as small as in the mentioned page: http://www.pfannenwelt.com/r/60262-steak-auf-spargel.html
I show you an example of a clean page as I see it: http://www.rankvilo.org/q/ips-and-domains
These are not the colors I want but they all fit together. I also need the font larger and the basic color scheme must be warmer. But maybe you can understand where I'm going or where I want to go.
Please do it very simple, with no corners, as flat and clean as possible, with a genuine feeling on first site of where the content is, what the focus of the site is (content).
Thank's.
Target Market(s)
age 35-55, majority is female, interested in recipes, cooking, baking
Industry/Entity Type
Media
Look and feel

```html
<!DOCTYPE html>
<html lang="de">
<head>
<meta charset="utf-8">
<title>Pfannenwelt – Steak auf Spargel</title>
<link href="https://fonts.googleapis.com/css2?family=PT+Sans:ital,wght@0,400;0,700;1,400;1,700&family=Lora:ital,wght@0,400;0,700;1,400;1,700&display=swap" rel="stylesheet">
<style>
:root{
  --maroon:#6a0606;
  --red:#8c1212;
  --red-soft:#a3301e;
  --cream:#fcf2dd;
  --footer:#f3e8d2;
  --panel:#ffffff;
  --line:#e5dcc8;
  --beige:#e7dbbd;
  --frame:#e4d7b4;
  --green:#6aa62e;
  --orange:#e08a12;
  --ink:#2a2220;
  --muted:#8a8078;
  --sans:"PT Sans",Arial,sans-serif;
  --serif:"Lora",Georgia,serif;
}
*{box-sizing:border-box;margin:0;padding:0}
html,body{width:694px;height:1200px;overflow:hidden}
body{background:var(--maroon);font-family:var(--sans);color:var(--ink);position:relative}
.abs{position:absolute}
.page{left:26px;top:0;width:642px;height:1145px;background:var(--cream)}
.login{left:516px;top:0;width:137px;height:20px;background:var(--maroon);color:#fff;font-size:9px;line-height:20px;text-align:center}
.logo{left:42px;top:34px;font-size:29px;font-weight:700;color:var(--red);letter-spacing:-.5px;display:flex;align-items:center;gap:6px}
.logo-dot{width:10px;height:10px;background:var(--red);border-radius:50%}
.search{left:466px;top:42px;width:192px;height:24px;border:1px solid #d8d0c4;border-radius:12px;background:#fff;box-shadow:inset 0 2px 3px rgba(0,0,0,.08);font-size:9px;color:#999;line-height:22px;padding-left:9px}
.search svg{position:absolute;right:7px;top:4px}
.nav{left:40px;top:75px;width:613px;height:31px;background:var(--red);border:2px solid var(--maroon);display:flex;align-items:center;padding-left:13px;gap:0}
.nav a{color:#fff;text-decoration:none;font-size:10.5px;padding:3px 13px;margin-right:2px}
.nav a.active{background:#5a0808;border-radius:2px}
.crumb{left:55px;top:126px;font-size:9px;color:#333}
.hero{left:50px;top:146px;width:382px;height:208px;background:var(--frame);padding:4px}
.hero-img{width:100%;height:100%;background:linear-gradient(180deg,#cfe3e6 0%,#e8d6a4 35%,#c98d3a 70%,#b56a22 100%);position:relative}
.hero-cap{position:absolute;left:0;right:0;bottom:0;height:46px;background:rgba(255,250,240,.72);padding:6px 0 0 7px}
.hero-cap h1{font-size:19px;font-weight:400;color:#222;line-height:20px}
.hero-cap p{font-size:9px;font-weight:700;color:var(--red);margin-top:1px}
.arrow{position:absolute;top:88px;width:18px;height:28px;background:var(--maroon);display:flex;align-items:center;justify-content:center}
.tools{left:315px;top:367px;display:flex;gap:8px}
.box{background:var(--panel);border:1px solid var(--line)}
.bar-title{background:var(--maroon);color:#fff;font-size:15px;height:19px;line-height:19px;padding-left:14px;margin:2px 1px 0}
.rating{left:452px;top:150px;width:189px;height:78px}
.stars{position:absolute;left:16px;top:24px;display:flex;gap:2px}
.votes{position:absolute;left:16px;top:40px;font-size:8px}
.share{position:absolute;top:57px;height:14px;border:1px solid #c7cbd4;border-radius:2px;font-size:7.5px;line-height:12px;padding:0 4px;background:#eef1f6;color:#3b5998}
.count{position:absolute;top:57px;height:14px;border:1px solid #bbb;border-radius:3px;font-size:7.5px;line-height:12px;padding:0 4px;background:#fff}
.info{left:452px;top:240px;width:189px;height:152px;font-size:8px}
.info .lvl{position:absolute;left:16px;top:27px;font-size:10px}
.info hr{position:absolute;left:16px;width:165px;border:0;border-top:1px solid #ddd}
.kv{position:absolute;left:16px;line-height:10.5px}
.kv span{position:absolute;left:64px;white-space:nowrap}
.sec-title{font-family:var(--serif);font-style:italic;color:var(--red);font-size:17px;text-decoration:underline;text-decoration-thickness:1px;text-underline-offset:3px}
.related{left:452px;top:403px;width:189px;height:222px}
.related .sec-title{position:absolute;left:17px;top:3px}
.rel{position:absolute;left:11px;width:170px;height:52px}
.thumb{position:absolute;width:64px;height:52px;background:linear-gradient(160deg,#6a4a2a,#c99a55 55%,#3b2a1a);border:1px solid #bbb}
.rel h4{position:absolute;left:70px;top:-3px;font-family:var(--serif);font-style:italic;font-weight:400;color:var(--orange);font-size:11px}
.rel p{position:absolute;left:70px;top:13px;width:92px;font-size:8px;line-height:12.5px}
.rel .more{position:absolute;right:12px;top:40px;font-size:8px;color:#999;font-style:italic}
.tags{left:452px;top:636px;width:189px;height:212px}
.tags .bar-title{font-family:var(--serif);text-align:center;padding:0;height:22px;line-height:22px}
.tag{position:absolute;font-family:var(--serif);font-weight:700;color:var(--maroon);white-space:nowrap;text-decoration:underline;text-decoration-thickness:1px;text-underline-offset:2px}
.author{left:452px;top:858px;width:189px;height:92px;background:var(--beige)}
.author .sec-title{position:absolute;left:15px;top:6px;color:#222}
.author .thumb{left:11px;top:34px;width:64px;height:50px}
.author .name{position:absolute;left:87px;top:35px;font-family:var(--serif);font-style:italic;color:var(--orange);font-size:12px}
.author .all{position:absolute;left:88px;top:53px;font-size:9px;line-height:12px;width:80px}
.ad{left:453px;top:960px;width:187px;height:154px}
.ad-img{width:100%;height:105px;background:linear-gradient(135deg,#f1e7d8 0%,#eaa35a 45%,#f2ebe3 70%,#d9d2ca 100%)}
.ad-flag{position:absolute;right:0;top:48px;width:50px;height:30px;background:#d8102a;color:#fff;font-size:7px;font-weight:700;line-height:9px;padding:3px}
.ad-band{height:49px;background:#f08a1e;position:relative;color:#fff;font-size:8.5px;line-height:12px;padding:6px 0 0 10px}
.ad-brand{position:absolute;right:6px;top:20px;width:52px;height:20px;background:#fff;color:#c00;font-size:8px;font-weight:700;text-align:center;line-height:20px}
.ad-duty{position:absolute;right:6px;top:3px;font-size:6px;color:#fff;text-decoration:underline}
.ingr{left:48px;top:400px;width:380px;height:337px}
.ingr .sec-title{position:absolute;left:13px;top:7px}
.convert{position:absolute;left:237px;top:6px;width:129px;height:24px;border:1px solid #d6d0c6;border-radius:12px;background:linear-gradient(#fff,#efebe4);font-family:var(--serif);font-style:italic;font-weight:700;font-size:9px;color:var(--maroon);line-height:22px;padding-left:8px}
.convert svg{position:absolute;right:9px;top:8px}
.row{position:absolute;left:13px;font-size:10px;white-space:nowrap}
.row b{font-weight:400;position:absolute;left:32px}
.row.sm{font-size:8.5px}
.extra{position:absolute;left:13px;top:171px;font-size:11px;color:var(--red);text-decoration:underline}
.photo-back{position:absolute;left:218px;top:74px;width:140px;height:170px;background:#e9b84a;transform:rotate(-5deg)}
.photo{position:absolute;left:232px;top:84px;width:128px;height:160px;border:3px solid #3a3a3a;background:linear-gradient(180deg,#f0ece6 0%,#e7c7a8 40%,#d2a36e 70%,#f3efe8 100%)}
.btn{position:absolute;top:310px;height:16px;background:linear-gradient(#a01818,var(--maroon));border-radius:3px;color:#fff;font-family:var(--serif);font-style:italic;font-weight:700;font-size:9px;line-height:16px;text-align:center}
.prep{left:48px;top:747px;width:380px;height:323px}
.prep .sec-title{position:absolute;left:11px;top:6px}
.step{position:absolute;left:13px;width:350px;font-size:8.5px;line-height:17px;padding-left:16px}
.step i{position:absolute;left:0;top:-3px;font-style:normal;font-size:22px;font-weight:700;color:var(--green);line-height:22px}
.step em{font-family:var(--serif);font-size:12px;color:var(--green);margin-right:4px}
.step em.inl{font-size:11px}
.bon{position:absolute;right:24px;top:301px;font-family:var(--serif);font-style:italic;color:var(--red);font-size:9.5px}
.notes{left:60px;top:1075px;font-size:8.5px;line-height:18px}
.notes h5{font-family:var(--serif);font-style:italic;color:var(--red);font-size:9px;font-weight:400}
.footer{left:26px;top:1145px;width:642px;height:30px;background:var(--footer);border-top:1px solid #e0d4bc;display:flex;justify-content:center;align-items:center;font-size:9px;gap:15px}
.copy{left:0;top:1183px;width:694px;text-align:center;font-size:8.5px;color:#e3a49a}
</style>
</head>
<body>
<div class="abs page"></div>
<div class="abs login">Login &nbsp;/&nbsp; kostenlos registrieren</div>
<div class="abs logo"><span class="logo-dot"></span>Pfannenwelt</div>
<div class="abs search">Search
  <svg width="13" height="13" viewBox="0 0 13 13"><circle cx="5" cy="5" r="4" fill="none" stroke="#555" stroke-width="1.6"/><line x1="8" y1="8" x2="12" y2="12" stroke="#555" stroke-width="2"/></svg>
</div>
<nav class="abs nav"><a class="active">Start</a><a>Rezepte</a><a>Magazin</a><a>Foren</a><a>Gemeinschaft</a><a>Markt</a></nav>
<div class="abs crumb">Pfannenwelt &gt;&gt; Start</div>

<div class="abs hero">
  <div class="hero-img" role="img" aria-label="Foto: gebratene Nudeln mit Paprika und Kräutern">
    <div class="arrow" style="left:0"><svg width="8" height="12"><path d="M7 1 2 6l5 5" stroke="#fff" stroke-width="2.5" fill="none"/></svg></div>
    <div class="arrow" style="right:0"><svg width="8" height="12"><path d="M1 1l5 5-5 5" stroke="#fff" stroke-width="2.5" fill="none"/></svg></div>
    <div class="hero-cap"><h1>Steak auf Spargel</h1><p>wunderbar, alle Zutaten sind geputzt gewogen</p></div>
  </div>
</div>

<div class="abs tools">
  <svg width="15" height="14"><rect x="1" y="1" width="13" height="12" fill="none" stroke="#8c1212" stroke-width="1.5"/><path d="M1 5h13M5 5v8M10 5v8" stroke="#8c1212"/></svg>
  <svg width="17" height="14"><path d="M1 2h3l2 8h8l2-6H5" fill="none" stroke="#8c1212" stroke-width="1.8"/><circle cx="7" cy="12.5" r="1.3" fill="#8c1212"/><circle cx="13" cy="12.5" r="1.3" fill="#8c1212"/></svg>
  <svg width="14" height="14"><path d="M1 1h12v10H8l-3 3v-3H1z" fill="#8c1212"/><rect x="6" y="3" width="2" height="4" fill="#fff"/><rect x="6" y="8" width="2" height="1.6" fill="#fff"/></svg>
  <svg width="16" height="14"><rect x="4" y="1" width="8" height="4" fill="#8c1212"/><rect x="1" y="5" width="14" height="6" fill="#8c1212"/><rect x="4" y="9" width="8" height="5" fill="#8c1212" stroke="#fff"/></svg>
  <svg width="17" height="14"><rect x="1" y="3" width="15" height="10" rx="1" fill="#8c1212"/><rect x="5" y="1" width="6" height="3" fill="#8c1212"/><circle cx="8.5" cy="8" r="3" fill="#fff"/><circle cx="8.5" cy="8" r="1.6" fill="#8c1212"/></svg>
</div>

<section class="abs box rating">
  <div class="bar-title">Rezeptbewertung</div>
  <div class="stars">
    <svg width="60" height="12" viewBox="0 0 60 12"><g fill="#e8902a"><path id="s" d="M6 0l1.8 3.9 4.2.4-3.2 2.8 1 4.1L6 9.1 2.2 11.2l1-4.1L0 4.3l4.2-.4z"/><use href="#s" x="12"/><use href="#s" x="24"/><use href="#s" x="36"/><use href="#s" x="48"/></g></svg>
  </div>
  <div class="votes">(ø 4 / 3 Stimmen) bewerten</div>
  <div class="share" style="left:12px">Recommend</div><div class="count" style="left:75px">10</div>
  <div class="share" style="left:101px;color:#333">+1</div><div class="count" style="left:122px">25</div>
</section>

<section class="abs box info">
  <div class="bar-title">Rezept Info</div>
  <div class="lvl">Schwierigkeit: Hobbykoch</div>
  <hr style="top:43px">
  <div class="kv" style="top:51px">Rezept-ID:<span>60262</span><br>eingetragen am:<span>02.06.09</span></div>
  <hr style="top:79px">
  <div class="kv" style="top:85px">angesehen:<span>4.364</span><br>gedruckt:<span>355</span><br>gespeichert:<span>84</span><br>versendet:<span>1</span></div>
</section>

<section class="abs box related">
  <h3 class="sec-title">Rezept Info</h3>
  <div class="rel" style="top:33px"><div class="thumb" role="img" aria-label="Foto: Steak-Kebab"></div><h4>Steak-Kebab</h4><p>Lorem Ipsum is simply dummy text of .....</p><span class="more">more...</span></div>
  <div class="rel" style="top:96px"><div class="thumb" role="img" aria-label="Foto: Steak-Kebab"></div><h4>Steak-Kebab</h4><p>Lorem Ipsum is simply dummy text of .....</p><span class="more">more...</span></div>
  <div class="rel" style="top:159px"><div class="thumb" role="img" aria-label="Foto: Steak-Kebab"></div><h4>Steak-Kebab</h4><p>Lorem Ipsum is simply dummy text of .....</p><span class="more">more...</span></div>
</section>

<section class="abs box tags">
  <div class="bar-title">Schlagworte</div>
  <span class="tag" style="left:12px;top:33px;font-size:10px;font-weight:400">Sprossengemüse</span>
  <span class="tag" style="left:99px;top:29px;font-size:15px">Rind</span>
  <span class="tag" style="left:17px;top:58px;font-size:11px">Obst</span>
  <span class="tag" style="left:68px;top:54px;font-size:14px">Gemüse und</span>
  <span class="tag" style="left:38px;top:79px;font-size:11px">Aufläufe und Souffles</span>
  <span class="tag" style="left:7px;top:99px;font-size:14px">Abendessen</span>
  <span class="tag" style="left:100px;top:104px;font-size:9px">Steak</span>
  <span class="tag" style="left:7px;top:125px;font-size:11px">Fleischgerichte</span>
  <span class="tag" style="left:100px;top:122px;font-size:15px">Spargel</span>
  <span class="tag" style="left:36px;top:149px;font-size:15px">Hauptgerichte</span>
  <span class="tag" style="left:11px;top:178px;font-size:11px">Überbackenes</span>
  <span class="tag" style="left:109px;top:180px;font-size:9px">gratinieren</span>
</section>

<section class="abs author">
  <h3 class="sec-title">Autor</h3>
  <div class="thumb" role="img" aria-label="Foto des Autors: Gericht"></div>
  <div class="name">herdfee</div>
  <div class="all">alle Rezepte von herdfee</div>
</section>

<aside class="abs ad">
  <div class="ad-img" role="img" aria-label="Werbefoto: zwei Frauen beim Sport mit Gymnastikball"></div>
  <div class="ad-flag">Mit tollen Rezepten und Bewegungs-übungen!</div>
  <div class="ad-band"><span class="ad-duty">Pflichttext</span>Jetzt Abnehm-Tagebuch<br>downloaden! Hier klicken!<div class="ad-brand">vitaform</div></div>
</aside>

<section class="abs box ingr">
  <h2 class="sec-title">Zutaten für 2 Portionen</h2>
  <div class="convert">Portionen umrechnen<svg width="8" height="5"><path d="M0 0h8L4 5z" fill="#333"/></svg></div>
  <div class="row" style="top:38px">2<b>Rinderhüft-Steaks á ca. 180 Gramm</b></div>
  <div class="row" style="top:55px">2 EL<b>Olivenöl</b></div>
  <div class="row" style="top:71px">10 g<b>Butter</b></div>
  <div class="row" style="top:88px"><b>Rosmarin, Salz,</b></div>
  <div class="row" style="top:104px"><b>Pfeffer, frisch gemörsert</b></div>
  <div class="row" style="top:121px">800 g<b>Spargel</b></div>
  <div class="row" style="top:138px">1 TL<b>Salz</b></div>
  <div class="row" style="top:155px">1 TL<b>Zucker</b></div>
  <div class="extra">Außerdem</div>
  <div class="row sm" style="top:189px">80 g<b>Gryerzer, gerieben</b></div>
  <div class="row sm" style="top:205px">500 g<b>Kartoffeln</b></div>
  <div class="row sm" style="top:222px">200 g<b>Kirschtomaten</b></div>
  <div class="row sm" style="top:239px">1<b>Knoblauchzehe</b></div>
  <div class="row sm" style="top:255px"><b>Salz, Pfeffer</b></div>
  <div class="row sm" style="top:272px"><b>Kräuter der Provence</b></div>
  <div class="row sm" style="top:289px"><b>Basilikum</b></div>
  <div class="row sm" style="top:306px">4 TL<b>Pesto</b></div>
  <div class="photo-back"></div>
  <div class="photo" role="img" aria-label="Foto: Frau mit einem Burger in der Hand"></div>
  <div class="btn" style="left:197px;width:68px">Einheiten</div>
  <div class="btn" style="left:281px;width:68px">Zutatenliste</div>
</section>

<section class="abs box prep">
  <h2 class="sec-title">Zubereitung</h2>
  <div class="step" style="top:39px"><i>*</i><em>Spargel</em> schälen, Wasser mit Salz, Zucker aufsetzen. Spargel darin einmal aufkochen und auf abgeschalteter Herdplatte ca. 10 Min. ziehen lassen.<br>Aus dem Wasser nehmen, abtropfen lassen.</div>
  <div class="step" style="top:95px"><i>*</i><em>Kartoffeln</em> schälen, vierteln, ca. 20 Min. in Salzwasser köcheln, abschütten, ausdampfen lassen</div>
  <div class="step" style="top:137px"><i>*</i>Pfanne erhitzen, Olivenöl, Butter und Rosamrin zugeben, die <em class="inl">Steaks</em>pro Seite ca. 2 Min. braten, raus aus der Pfanne, salzen, pfeffern</div>
  <div class="step" style="top:177px"><i>*</i>den Spargel in eine Auflaufform schichten, Kartoffeln "drumrum" legen<br>zart salzen, mit den Kräutern bestreuen</div>
  <div class="step" style="top:219px"><i>*</i>Steak obenauf legen, mit dem Pesto bestreichen, die halbierten Tomaten, Knoblauch und Basilikum, dem Käse und den Kräuter der Provence, Salz und Pfeffer bestreuen</div>
  <div class="step" style="top:261px"><i>*</i>Backofen auf 225°C vorheizen, runterschalten auf 180°C,<br>Auflauf 20 Min. überbacken. Das Steak ist dann zartrosa</div>
  <div class="bon">Guten Appetit</div>
</section>

<div class="abs notes">
  <h5>Geräte und Anmerkungen des Autors</h5>
  Sie benötigen: Reibe für Käse<br>Herkunft des Rezepts: KV, Herdgötter.de
</div>

<footer class="abs footer"><span>Start</span>|<span>Rezepte</span>|<span>Magazin</span>|<span>Foren</span>|<span>Gemeinschaft</span>|<span>Markt</span></footer>
<div class="abs copy">© 2012 Pfannenwelt.com. All right reserved.</div>
</body>
</html>
```